Tri-fold brochue, business card, and stationary design.

Tri-fold brochure: We are looking to get a tri-fold brochure template created so we can add our content on each side of the brochure and then leave these with prospective clients during sales calls.Business card: We would like the business card to have employee name, phone number, and email address on the card. We are open to rounded corners as well.We just redid our website and we'd like all designs to be complementary to our new "Look and feel" of our website.

Contact Information for Business Card

We would like the business card to have employee name, phone number, and email address on the card. We are open to rounded corners as well.

We just redid our website and we'd like all designs to be complementary to our new "Look and feel" of our website.

```html
<!DOCTYPE html>
<html lang="en">
<head>
<meta charset="utf-8">
<title>Harborline Networks – Business Card</title>
<link href="https://fonts.googleapis.com/css2?family=Exo+2:wght@400;500;600&display=swap" rel="stylesheet">
<style>
  :root {
    --canvas: #eceff1;
    --paper: #ffffff;
    --paper-shade: #f1f3f4;
    --cyan: #2fb6dc;
    --cyan-light: #5cc9e8;
    --blue-deep: #1677a3;
    --blue-mid: #1f93c2;
    --rule: #b9dbe8;
  }
  * { box-sizing: border-box; margin: 0; padding: 0; }
  html, body { width: 1200px; height: 1023px; overflow: hidden; }
  body {
    background: var(--canvas);
    font-family: "Exo 2", sans-serif;
    position: relative;
  }
  .card {
    position: absolute;
    left: 240px;
    width: 720px;
    height: 410px;
    border-radius: 30px;
    overflow: hidden;
    box-shadow: 0 10px 28px rgba(0,0,0,.14);
  }
  /* Front */
  .card-front {
    top: 60px;
    background: linear-gradient(135deg, var(--paper) 55%, var(--paper-shade));
  }
  .front-content {
    position: absolute;
    left: 0; top: 0;
    width: 602px; height: 100%;
  }
  .front-band {
    position: absolute;
    top: 0; right: 0;
    width: 118px; height: 100%;
    background: linear-gradient(90deg, var(--cyan-light), var(--blue-mid));
  }
  .front-band::before {
    content: "";
    position: absolute;
    left: 0; top: 0;
    width: 30px; height: 100%;
    background: rgba(255,255,255,.18);
  }
  .brand {
    position: absolute;
    left: 64px; top: 84px;
    display: flex; align-items: center; gap: 18px;
    white-space: nowrap;
  }
  .brand-dot {
    width: 64px; height: 64px;
    border-radius: 50%;
    background: var(--cyan);
    flex: none;
  }
  .brand-name {
    color: var(--cyan);
    font-weight: 600;
    font-size: 34px;
    line-height: 1;
    letter-spacing: .3px;
  }
  .person {
    position: absolute;
    left: 64px; top: 222px;
    color: var(--cyan);
    white-space: nowrap;
  }
  .person-name { font-size: 34px; font-weight: 500; line-height: 1.05; }
  .person-role { font-size: 21px; font-weight: 400; margin-top: 8px; padding-left: 100px; }
  .person-phone { font-size: 22px; font-weight: 400; margin-top: 6px; padding-left: 84px; letter-spacing: .8px; }
  .divider {
    position: absolute;
    left: 332px; top: 214px;
    width: 1px; height: 128px;
    background: var(--rule);
  }
  .contacts {
    position: absolute;
    left: 348px; top: 218px;
    width: 236px;
    list-style: none;
    color: var(--cyan);
    font-size: 13px;
    line-height: 1.25;
    white-space: nowrap;
  }
  .contacts li { display: flex; align-items: center; gap: 10px; margin-bottom: 12px; }
  .contact-icon {
    width: 26px; height: 26px; flex: none;
    border-radius: 50%;
    background: var(--cyan);
    display: flex; align-items: center; justify-content: center;
  }
  /* Back */
  .card-back {
    top: 552px;
    background: linear-gradient(135deg, var(--blue-deep), var(--blue-mid) 55%, var(--cyan));
  }
  .back-brand {
    position: absolute;
    inset: 0;
    display: flex; align-items: center; justify-content: center; gap: 24px;
  }
  .back-dot {
    width: 96px; height: 96px; border-radius: 50%;
    background: var(--paper);
  }
  .back-name {
    color: var(--paper);
    font-weight: 600;
    font-size: 50px;
    line-height: 1;
  }
</style>
</head>
<body>
  <section class="card card-front" aria-label="Business card front">
    <div class="front-content">
      <div class="brand">
        <span class="brand-dot"></span>
        <span class="brand-name">Harborline Networks</span>
      </div>

      <div class="person">
        <p class="person-name">Your Name here</p>
        <p class="person-role">Designation</p>
        <p class="person-phone">012 345 67890</p>
      </div>

      <span class="divider"></span>

      <ul class="contacts">
        <li>
          <span class="contact-icon">
            <svg width="14" height="10" viewBox="0 0 14 10"><rect x="0.5" y="0.5" width="13" height="9" fill="#fff"/><path d="M0.5 0.5 L7 5.5 L13.5 0.5" fill="none" stroke="#2fb6dc" stroke-width="1.2"/></svg>
          </span>
          <span>info@harborlinenet.com</span>
        </li>
        <li>
          <span class="contact-icon">
            <svg width="14" height="13" viewBox="0 0 14 13"><path d="M7 0 L14 6 H12 V13 H8.5 V9 H5.5 V13 H2 V6 H0 Z" fill="#fff"/></svg>
          </span>
          <span>your city address here,<br>street location, NY city, USA</span>
        </li>
        <li>
          <span class="contact-icon">
            <svg width="14" height="14" viewBox="0 0 14 14" fill="none" stroke="#fff" stroke-width="1.3"><circle cx="7" cy="7" r="6"/><ellipse cx="7" cy="7" rx="2.6" ry="6"/><path d="M1 7 H13"/></svg>
          </span>
          <span>www.harborlinenet.com</span>
        </li>
      </ul>
    </div>

    <div class="front-band"></div>
  </section>

  <section class="card card-back" aria-label="Business card back">
    <div class="back-brand">
      <span class="back-dot"></span>
      <span class="back-name">Harborline Networks</span>
    </div>
  </section>
</body>
</html>
```